Small Business Consulting Firm Needs Business Card Design

Need a sleek modern business card with 2 sides matching the colors of our logo. We will be placing these with a mailer we are sending out. These business cards will only ever be given to business owners. We operate helping businesses who are struggling with cash flow or finances. If the green and blue design needs to be moved to the right of "Harborline Crest Consulting" for aesthetic purposes that is ok. We will need an editable file if possible. We would like to include the reps name, email, website, and phone number. For now just use Peter Vance, pvance@harborlinecrest.com, www.harborlinecrest.com, and 833-555-0172.

```html
<!DOCTYPE html>
<html lang="en">
<head>
<meta charset="utf-8">
<title>Harborline Crest Consulting – Business Card</title>
<link href="https://fonts.googleapis.com/css2?family=Lato:wght@400;700&display=swap" rel="stylesheet">
<style>
  :root {
    --page: #f1f1f1;
    --card: #ffffff;
    --ink: #3a3a3a;
    --ink-dark: #1f1f1f;
    --green: #6ab547;
    --green-light: #8cc96b;
  }
  * { margin: 0; padding: 0; box-sizing: border-box; }
  html, body {
    width: 1200px;
    height: 757px;
    overflow: hidden;
    background: var(--page);
    font-family: "Lato", sans-serif;
    color: var(--ink);
  }
  .canvas { position: relative; width: 1200px; height: 757px; }
  .card {
    position: absolute;
    top: 196px;
    width: 498px;
    height: 298px;
    background: var(--card);
    box-shadow: 0 1px 3px rgba(0,0,0,0.08);
  }
  .card--front { left: 90px; }
  .card--back { left: 650px; }

  .brand { position: absolute; text-align: center; }
  .brand__mark { display: block; margin: 0 auto; background: var(--green); }
  .brand__name {
    font-weight: 400;
    color: var(--ink);
    text-transform: uppercase;
    line-height: 1.25;
  }

  .card--front .brand { left: 0; right: 0; top: 58px; }
  .card--front .brand__mark { width: 58px; height: 58px; margin-bottom: 26px; }
  .card--front .brand__name { font-size: 19px; letter-spacing: 3.5px; }

  .website {
    position: absolute;
    left: 0; right: 0; top: 266px;
    text-align: center;
    font-size: 13px;
    font-weight: 700;
    letter-spacing: 1.2px;
    color: var(--green);
  }

  .card--back .brand { left: 20px; width: 248px; top: 98px; }
  .card--back .brand__mark { width: 46px; height: 46px; margin-bottom: 24px; }
  .card--back .brand__name { font-size: 14px; letter-spacing: 2.6px; }

  .divider {
    position: absolute;
    left: 262px; top: 80px;
    width: 2px; height: 150px;
    background: linear-gradient(to bottom, rgba(106,181,71,0), var(--green) 30%, var(--green) 70%, rgba(106,181,71,0));
  }

  .contact { position: absolute; left: 299px; top: 110px; }
  .contact__name { font-size: 15px; color: var(--green); font-weight: 400; }
  .contact__role { font-size: 10px; font-weight: 700; color: var(--ink-dark); margin-top: 3px; }
  .contact__list { list-style: none; margin-top: 20px; }
  .contact__item {
    display: flex; align-items: center; gap: 8px;
    font-size: 10.5px; color: var(--ink-dark); height: 17px;
  }
  .contact__icon { width: 11px; height: 11px; fill: var(--green); flex: none; }
</style>
</head>
<body>
<div class="canvas">

  <section class="card card--front">
    <div class="brand">
      <span class="brand__mark"></span>
      <p class="brand__name">Harborline Crest<br>Consulting</p>
    </div>
    <p class="website">www.harborlinecrest.com</p>
  </section>

  <section class="card card--back">
    <div class="brand">
      <span class="brand__mark"></span>
      <p class="brand__name">Harborline Crest<br>Consulting</p>
    </div>
    <div class="divider"></div>
    <div class="contact">
      <p class="contact__name">Peter Vance</p>
      <p class="contact__role">Owner / Founder</p>
      <ul class="contact__list">
        <li class="contact__item">
          <svg class="contact__icon" viewBox="0 0 12 12" aria-hidden="true"><path d="M1 4c0-1.5 2-2.5 5-2.5S11 2.5 11 4v1H8.5V4h-5v1H1z M2.5 6h7l1 4.5h-9z M6 7a1.3 1.3 0 1 0 0 2.6A1.3 1.3 0 0 0 6 7z"/></svg>
          <span>(833) 555-0172</span>
        </li>
        <li class="contact__item">
          <svg class="contact__icon" viewBox="0 0 12 12" aria-hidden="true"><path d="M1 2.5h10v7H1z M1.6 3.2 6 6.6l4.4-3.4" stroke="#fff" stroke-width="0.9"/></svg>
          <span>pvance@harborlinecrest.com</span>
        </li>
      </ul>
    </div>
  </section>

</div>
</body>
</html>
```